Flat bootstrap design for existing site

I'm looking for a modern flat design based around an existing logo. This has to be a custom design (no external templates), and implemented into a bootstrap framework.

The logo is attached as 2 versions - choose whichever you want, that flows better with whatever design you choose.

Added screenshots of the existing site (currently using the default bootstrap layouts). Please make your designs around those pages in the screenshots (i.e. the homepage only has the postal code input and the header). The active page has 3 screenshots, because I wanted to illustrate the other states that would be visible (in the table rows).

This is a moving/junk removal website, just for some context.

Here's some example websites (flat designs) that I like, just to give you an idea of what I'm after.

https://www.plivento.com/
https://hoskadel.com/
https://trumvex.com/
https://bravolinth.com/en/

• It must be a modern/simple flat design, that is built around the existing logo (attached).
• It has to be implemented using bootstrap.

```html
<!DOCTYPE html>
<html lang="en">
<head>
<meta charset="utf-8">
<title>HAULVO – Booking Details</title>
<link href="https://fonts.googleapis.com/css2?family=Open+Sans:wght@400;600;700&display=swap" rel="stylesheet">
<style>
  :root {
    --sky: #4bc8f4;
    --white: #ffffff;
    --ink: #222222;
    --muted: #6d6d6d;
    --line: #cfcfcf;
    --row-line: #e6e6e6;
    --band: #e0e0e0;
    --amber: #f8a823;
  }
  * { box-sizing: border-box; margin: 0; padding: 0; }
  html, body { width: 1200px; height: 1118px; overflow: hidden; }
  body {
    position: relative;
    background: var(--sky);
    font-family: "Open Sans", sans-serif;
    color: var(--ink);
  }
  .site-header { position: absolute; top: 0; left: 0; width: 1200px; height: 84px; }
  .brand {
    position: absolute; left: 130px; top: 24px;
    display: flex; align-items: center; gap: 8px;
    color: var(--white); font-weight: 700; font-size: 28px; letter-spacing: 1px;
  }
  .brand-dot { width: 14px; height: 14px; border-radius: 50%; background: var(--white); }
  .nav-link {
    position: absolute; top: 34px; color: var(--white);
    font-size: 11.5px; font-weight: 700; letter-spacing: .2px;
  }
  .nav-cta {
    position: absolute; left: 764px; top: 28px; width: 127px; height: 27px;
    background: var(--white); color: var(--sky);
    font-size: 11.5px; font-weight: 700; display: flex; align-items: center; justify-content: center;
  }
  .user-avatar {
    position: absolute; left: 910px; top: 28px; width: 28px; height: 28px;
    border-radius: 50%; background: var(--white);
  }
  .user-email {
    position: absolute; left: 947px; top: 33px;
    color: var(--white); font-size: 12px; font-weight: 700;
  }
  .user-caret { position: absolute; left: 1061px; top: 39px; }

  .card {
    position: absolute; left: 130px; width: 940px; background: var(--white);
    box-shadow: 0 22px 26px -14px rgba(20, 100, 140, .55);
  }
  .booking-card { top: 93px; height: 507px; }
  .drivers-card { top: 651px; height: 338px; }
  .card-title { position: absolute; color: var(--sky); font-size: 25px; font-weight: 600; }
  .field-label { position: absolute; font-size: 13px; }
  .field {
    position: absolute; height: 51px; border: 1px solid var(--line);
    box-shadow: 0 8px 14px -6px rgba(0,0,0,.12);
    color: var(--muted); font-size: 13.5px; padding: 14px 18px;
  }
  .field-select { left: 49px; top: 124px; width: 386px; }
  .field-date { left: 487px; top: 124px; width: 386px; }
  .field svg { position: absolute; right: 18px; top: 14px; }
  .field-textarea { left: 49px; top: 244px; width: 827px; height: 139px; padding: 20px 17px; }
  .update-btn {
    position: absolute; left: 740px; top: 419px; width: 134px; height: 44px;
    background: var(--sky); color: var(--white); font-weight: 700; font-size: 16.5px;
    letter-spacing: .5px; display: flex; align-items: center; justify-content: center;
  }
  .drivers-intro { position: absolute; left: 41px; top: 63px; font-size: 12px; color: #333; }
  .drivers-table { position: absolute; left: 0; top: 111px; width: 939px; border-collapse: collapse; }
  .drivers-table th {
    background: var(--band); height: 34px; text-align: left;
    font-size: 12px; font-weight: 600;
  }
  .drivers-table td { font-size: 12px; border-bottom: 1px solid var(--row-line); }
  .drivers-table tr:last-child td { border-bottom: none; }
  .col-name { padding-left: 42px; width: 234px; }
  .col-dist { width: 211px; }
  .status-cell { text-align: right; padding-right: 63px; }
  .status-badge {
    display: inline-flex; align-items: center; gap: 9px;
    width: 105px; height: 26px; padding-left: 17px;
    background: var(--amber); color: var(--white); font-size: 11px; font-weight: 600;
  }
  .dash { display: inline-block; width: 11px; border-top: 1px solid var(--ink); transform: translateY(4px); }
  .site-footer {
    position: absolute; right: 12px; top: 1089px;
    display: flex; align-items: center; gap: 8px;
    color: var(--white); font-size: 11.5px;
  }
</style>
</head>
<body>
  <header class="site-header">
    <div class="brand"><span class="brand-dot"></span>HAULVO</div>
    <span class="nav-link" style="left:582px">BOOK</span>
    <span class="nav-link" style="left:649px">HOW IT WORKS</span>
    <span class="nav-cta">BECOME A DRIVER</span>
    <span class="user-avatar">
      <svg width="28" height="28" viewBox="0 0 28 28"><circle cx="14" cy="11" r="3.3" fill="#4bc8f4"/><path d="M8.5 19.5c0-3.5 2.5-5 5.5-5s5.5 1.5 5.5 5z" fill="#4bc8f4"/></svg>
    </span>
    <span class="user-email">dana@mailo.com</span>
    <svg class="user-caret" width="10" height="6" viewBox="0 0 10 6"><path d="M0 0h10L5 6z" fill="#fff"/></svg>
  </header>

  <section class="card booking-card">
    <h1 class="card-title" style="left:49px;top:30px">Booking Details</h1>
    <label class="field-label" style="left:49px;top:92px">Package Selected</label>
    <div class="field field-select">Package 1
      <svg width="12" height="22" viewBox="0 0 12 22"><path d="M1 6l5-5 5 5z M1 15l5 5 5-5z" fill="#4bc8f4"/></svg>
    </div>
    <label class="field-label" style="left:487px;top:92px">Pick up time selected</label>
    <div class="field field-date">Jult 18 at &nbsp;4:13 am
      <svg width="14" height="16" viewBox="0 0 14 16" style="top:16px"><rect x="1" y="3" width="12" height="12" fill="none" stroke="#4bc8f4" stroke-width="1.5"/><path d="M1 7h12M4 1v4M10 1v4" stroke="#4bc8f4" stroke-width="1.5"/></svg>
    </div>
    <label class="field-label" style="left:49px;top:206px">Description</label>
    <div class="field field-textarea">1 Large stove</div>
    <span class="update-btn">UPDATE</span>
  </section>

  <section class="card drivers-card">
    <h2 class="card-title" style="left:40px;top:29px">Drivers in your area</h2>
    <p class="drivers-intro">Please stay on this page and be patient, while we contact the drivers and find you one ASAP</p>
    <table class="drivers-table">
      <thead>
        <tr><th class="col-name">Name</th><th class="col-dist">Distance (km)</th><th>Agreed Pickup Time</th><th></th></tr>
      </thead>
      <tbody>
        <tr style="height:50px"><td class="col-name">Marlo Prent</td><td>4.04km Away</td><td><span class="dash"></span></td><td class="status-cell"><span class="status-badge"><svg width="9" height="9" viewBox="0 0 10 10"><circle cx="5" cy="5" r="4" fill="none" stroke="#fff" stroke-width="1.3"/><path d="M5 2.5V5h2" stroke="#fff" stroke-width="1.2" fill="none"/></svg>PENDING</span></td></tr>
        <tr style="height:45px"><td class="col-name">Tobin Askew</td><td>5.7km Away</td><td><span class="dash"></span></td><td class="status-cell"><span class="status-badge"><svg width="9" height="9" viewBox="0 0 10 10"><circle cx="5" cy="5" r="4" fill="none" stroke="#fff" stroke-width="1.3"/><path d="M5 2.5V5h2" stroke="#fff" stroke-width="1.2" fill="none"/></svg>PENDING</span></td></tr>
        <tr style="height:40px"><td class="col-name">Elden Varrow</td><td>11.13km Away</td><td><span class="dash"></span></td><td class="status-cell"><span class="status-badge"><svg width="9" height="9" viewBox="0 0 10 10"><circle cx="5" cy="5" r="4" fill="none" stroke="#fff" stroke-width="1.3"/><path d="M5 2.5V5h2" stroke="#fff" stroke-width="1.2" fill="none"/></svg>PENDING</span></td></tr>
        <tr style="height:44px"><td class="col-name">Wade Kellerby</td><td>11.91km Away</td><td><span class="dash"></span></td><td class="status-cell"><span class="status-badge"><svg width="9" height="9" viewBox="0 0 10 10"><circle cx="5" cy="5" r="4" fill="none" stroke="#fff" stroke-width="1.3"/><path d="M5 2.5V5h2" stroke="#fff" stroke-width="1.2" fill="none"/></svg>PENDING</span></td></tr>
      </tbody>
    </table>
  </section>

  <footer class="site-footer">
    <svg width="12" height="12" viewBox="0 0 12 12"><circle cx="6" cy="6" r="5.3" fill="none" stroke="#fff"/><path d="M7.8 4.4A2.3 2.3 0 1 0 7.8 7.6" fill="none" stroke="#fff"/></svg>
    Copyrights @ 2017 All Rights Reserved
  </footer>
</body>
</html>
```